vault key finders.com

we are a new company that offer people that have lost there bit coin transaction a recovery and retrieval service
We are looking for a website that will allow you to fill in your details

name
email
bitcoins or other crypto lost and date of transaction

and then an auto reply to them from a given email to verify there email

I am looking for an easy for the client to leave there interest and has a security look around it and looks familiar to the user.

https://purserestore.example/?ref=Xq7LmT2vNp9RsK4wYb8ZcD1fGh6JkM3nQe5UtV0aBy

https://pursemendingaid.example

https://www.zennoro.example/faq-items/restoring-your-token-purse/

Target Market(s)

early investors into crypto

Industry/Entity Type

It Company

Logo Text

VAULTKEY FINDERS/LOCATORS

Coding

Coded - Design and coding required

Number of Pages Required

3 page

Requirements
Must have
• be able to :
• complete
• Name,
• Email
• transaction date of exchange and how much they invested

```html
<!DOCTYPE html>
<html lang="en">
<head>
<meta charset="utf-8">
<title>VaultKey Finders — Wallet Recovery</title>
<link rel="stylesheet" href="https://fonts.googleapis.com/css2?family=Open+Sans:wght@400;600;700&family=Passion+One:wght@400&family=Roboto+Slab:wght@300&display=swap">
<style>
:root{
  --stage:#6b6b6b;
  --yellow:#f2d41c;
  --yellow-deep:#e8c20e;
  --yellow-btn:#f7d31a;
  --white:#ffffff;
  --ink:#222222;
  --muted:#8a8a8a;
  --rule:#e2e2e2;
  --blue:#2a8fd6;
  --black:#000000;
  --dark:#1e1e1e;
  --slate:#5a5a5a;
  --band:#ececec;
  --social:#2b5fb3;
}
*{margin:0;padding:0;box-sizing:border-box}
html,body{width:1200px;height:1200px;overflow:hidden;background:var(--stage);font-family:"Open Sans",sans-serif}
.page{position:absolute;left:239px;top:0;width:722px;height:1200px;background:var(--white);overflow:hidden}
.abs{position:absolute}

/* hero */
.hero{left:0;top:0;width:722px;height:366px;background:linear-gradient(100deg,#f4d927 0%,#eccf22 50%,#d9b91a 75%,#c8a918 100%)}
.hero-figure{left:400px;top:40px;width:322px;height:326px;background:radial-gradient(ellipse at 55% 40%,rgba(200,160,20,.55),rgba(242,212,28,0) 70%)}
.site-header{left:0;top:0;width:722px;height:54px;background:rgba(255,240,120,.35)}
.brand{left:94px;top:17px;display:flex;align-items:center;gap:6px;color:var(--white)}
.brand-mark{width:18px;height:18px;background:var(--white);opacity:.85}
.brand-name{font-weight:700;font-size:10px;letter-spacing:.6px;line-height:1}
.brand-url{font-size:4.5px;letter-spacing:.4px;margin-top:2px;font-weight:600}
.nav{left:286px;top:21px;display:flex;gap:0;font-size:6.2px;letter-spacing:.6px;color:rgba(255,255,255,.85)}
.nav span{margin-right:18px}
.nav .active{font-weight:700;color:var(--white)}
.inquire{left:559px;top:14px;width:69px;height:24px;background:var(--white);border:1px solid #ddd;font-size:5.6px;font-weight:700;letter-spacing:.5px;color:var(--ink);display:flex;align-items:center;justify-content:center}
.slider-arrows{left:598px;top:78px;color:var(--white);font-size:12px;display:flex;gap:12px}
.accent-bar{left:94px;top:115px;width:54px;height:5px;background:var(--white)}
.hero-title{left:93px;top:128px;font-family:"Passion One",sans-serif;font-size:30px;line-height:42px;letter-spacing:1.2px;color:var(--white)}
.hero-copy{left:97px;top:224px;width:282px;font-size:6.2px;line-height:10px;letter-spacing:.3px;color:rgba(255,255,255,.92)}
.btn-contact{left:94px;top:294px;width:92px;height:28px;background:var(--yellow-btn);box-shadow:0 1px 3px rgba(0,0,0,.15);color:var(--white);font-size:6.2px;font-weight:700;letter-spacing:.6px;display:flex;align-items:center;justify-content:center}
.btn-more{left:205px;top:304px;color:var(--white);font-size:6.2px;font-weight:700;letter-spacing:.6px;display:flex;align-items:center;gap:5px}
.dots{left:591px;top:334px;display:flex;gap:3px}
.dots i{display:block;width:10px;height:1.5px;background:rgba(255,255,255,.5)}
.dots i:first-child{background:var(--white)}

/* services */
.band-light{left:0;top:366px;width:722px;height:280px;background:var(--band)}
.services{left:94px;top:350px;width:534px;height:264px;background:var(--white)}
.services-top{left:0;top:0;width:534px;height:2px;background:linear-gradient(90deg,var(--rule) 0 25%,var(--yellow) 25% 50%,var(--rule) 50% 75%,var(--yellow) 75%)}
.section-label{left:27px;top:28px;font-size:8.2px;font-weight:600;letter-spacing:.6px;color:var(--ink)}
.section-label-rule{left:27px;top:42px;width:64px;height:1px;background:var(--rule)}
.card{top:56px;width:155px}
.card-media{width:155px;height:90px;border:1px solid #cfcfcf}
.media-wallet{background:linear-gradient(135deg,#c9a7a4,#5a4a44 55%,#2a2a2a)}
.media-tools{background:linear-gradient(135deg,#6b5238,#3d2d1f 60%,#54402b)}
.media-thinker{background:linear-gradient(90deg,#ffffff 30%,#e6e2de 55%,#2c3547 80%,#ffffff)}
.card-title{margin-top:14px;font-size:6.3px;font-weight:700;letter-spacing:.6px;color:var(--blue);padding-bottom:6px;border-bottom:1px solid var(--rule)}
.card-copy{margin-top:9px;font-size:6.3px;line-height:11px;letter-spacing:.3px;color:var(--muted)}
.card-link{margin-top:9px;display:flex;align-items:center;gap:6px;font-size:5px;font-weight:700;letter-spacing:.6px;color:var(--muted)}
.card-link b{flex:1;height:1px;background:var(--rule);margin-left:10px}

/* about */
.band-dark{left:0;top:646px;width:722px;height:446px;background:linear-gradient(180deg,#4a4a4a,#6e6e6e 40%,#5c5c5c 80%,#4d4d4d)}
.about-side{left:94px;top:614px;width:180px;height:288px;background:var(--black)}
.about-side .rule-top{left:13px;top:13px;width:154px;height:1px;background:#333}
.about-side .rule-bottom{left:13px;top:274px;width:154px;height:1px;background:#333}
.side-brand{left:22px;top:133px;display:flex;align-items:center;gap:6px;color:var(--white)}
.side-brand .brand-mark{width:22px;height:22px;opacity:1}
.side-brand .brand-name{font-size:9.5px;letter-spacing:.8px}
.blog-link{left:19px;top:257px;font-size:5.8px;font-weight:700;letter-spacing:.6px;color:var(--white)}
.about-main{left:274px;top:614px;width:354px;height:288px;background:linear-gradient(120deg,#262626,#3a3a3a 60%,#2a2a2a)}
.about-eyebrow{left:75px;top:27px;font-size:5.4px;font-weight:700;letter-spacing:.6px;color:var(--white)}
.about-eyebrow-rule{left:126px;top:30px;width:210px;height:1px;background:#4a4a4a}
.about-title{left:34px;top:66px;font-family:"Roboto Slab",serif;font-weight:300;font-size:17px;letter-spacing:1px;color:var(--yellow)}
.about-copy{left:42px;top:98px;width:240px;font-size:6.3px;line-height:11px;letter-spacing:.3px;color:#dcdcdc}
.about-dots{left:292px;top:152px;display:flex;gap:3px}
.about-dots i{width:14px;height:1.5px;background:#888;display:block}
.about-media{left:35px;top:162px;width:304px;height:110px;border:1px solid #ddd;background:linear-gradient(100deg,#e9e6df 0%,#d7c59a 25%,#e8c53a 45%,#f0cf45 65%,#b89c7d 85%,#8f7a68 100%)}

/* callback */
.callback-title{left:0;top:932px;width:722px;text-align:center;font-family:"Roboto Slab",serif;font-weight:300;font-size:19px;letter-spacing:1px;color:var(--white)}
.callback-sub{left:0;top:965px;width:722px;text-align:center;font-size:7.6px;letter-spacing:.6px;color:#e6e6e6}
.field{top:996px;width:172px;height:29px;border-bottom:1px solid #bdbdbd}
.field label{display:block;padding-left:4px;font-size:5.2px;font-weight:700;letter-spacing:.6px;color:var(--white)}
.send{left:340px;top:1042px;width:42px;height:29px;background:var(--blue);color:var(--white);font-size:5.8px;font-weight:700;letter-spacing:.6px;display:flex;align-items:center;justify-content:center}

/* footer */
.footer{left:0;top:1092px;width:722px;height:108px;background:var(--white)}
.copyright{left:94px;top:43px;font-size:7px;font-weight:700;letter-spacing:.7px;line-height:13px;color:var(--ink)}
.social{left:346px;top:47px;display:flex;gap:2px}
.social i{display:block;width:15px;height:15px;background:var(--social)}
.footer-url{left:400px;top:50px;width:228px;text-align:right;font-size:7px;font-weight:700;letter-spacing:.7px;color:var(--ink)}
</style>
</head>
<body>
<main class="page">

  <section class="abs hero">
    <div class="abs hero-figure" role="img" aria-label="Woman in a yellow blouse talking on a phone, tinted yellow over a network of connected coin shapes"></div>
    <header class="abs site-header"></header>
    <div class="abs brand">
      <span class="brand-mark"></span>
      <div><div class="brand-name">VAULTKEY FINDERS</div><div class="brand-url">www.vaultkey-finders.com</div></div>
    </div>
    <nav class="abs nav"><span class="active">HOME</span><span>SERVICES</span><span>PRODUCTS</span><span>WHO WE ARE</span><span>ABOUT US</span></nav>
    <div class="abs inquire">INQUIRE NOW</div>
    <div class="abs slider-arrows">
      <svg width="8" height="10" viewBox="0 0 8 10"><path d="M6 1 2 5l4 4" fill="none" stroke="#fff" stroke-width="1.4"/></svg>
      <svg width="8" height="10" viewBox="0 0 8 10"><path d="M2 1l4 4-4 4" fill="none" stroke="#fff" stroke-width="1" opacity=".7"/></svg>
    </div>
    <div class="abs accent-bar"></div>
    <h1 class="abs hero-title">HAVE YOU FORGOTTEN YOUR<br>WALLET PASSWORD?</h1>
    <p class="abs hero-copy">Bitcoin and Ethereum wallets are normally encrypted by you, the wallet owner. However, sometimes you forget or misplace your wallet password. This is a bad thing! Unless the password is recovered, you have no way to access any funds stored in that wallet. That money is lost forever. At today's exchange rate, that might be a lot of money.</p>
    <div class="abs btn-contact">CONTACT US NOW!</div>
    <div class="abs btn-more">LEARN MORE
      <svg width="13" height="5" viewBox="0 0 13 5"><path d="M0 2.5h11M9 .5l2.5 2-2.5 2" fill="none" stroke="#fff" stroke-width="1.2"/></svg>
    </div>
    <div class="abs dots"><i></i><i></i><i></i></div>
  </section>

  <div class="abs band-light"></div>
  <section class="abs services">
    <div class="abs services-top"></div>
    <h2 class="abs section-label">Featured Services</h2>
    <div class="abs section-label-rule"></div>

    <article class="abs card" style="left:27px">
      <div class="card-media media-wallet" role="img" aria-label="Hands pulling banknotes from a black leather wallet"></div>
      <h3 class="card-title">RECOVERING YOUR BITCOIN WALLET</h3>
      <p class="card-copy">Far far away, behind the word mountains, far from the countries Vokalia and Consonantia, there live the blind texts.</p>
      <div class="card-link">LEARN MORE <svg width="12" height="4" viewBox="0 0 12 4"><path d="M0 2h10M8 .3 11 2 8 3.7" fill="none" stroke="#8a8a8a"/></svg><b></b></div>
    </article>

    <article class="abs card" style="left:190px">
      <div class="card-media media-tools" role="img" aria-label="Hammer, pliers and hand tools on a dark wooden workbench"></div>
      <h3 class="card-title">WHAT YOU'LL NEED</h3>
      <p class="card-copy">Far far away, behind the word mountains, far from the countries Vokalia and Consonantia, there live the blind texts.</p>
      <div class="card-link">LEARN MORE <svg width="10" height="4" viewBox="0 0 10 4"><path d="M0 2h8M6 .3 9 2 6 3.7" fill="none" stroke="#8a8a8a"/></svg><b></b></div>
    </article>

    <article class="abs card" style="left:353px">
      <div class="card-media media-thinker" role="img" aria-label="Man in a dark suit thinking, on a white background"></div>
      <h3 class="card-title">HOW TO DO IT?</h3>
      <p class="card-copy">Far far away, behind the word mountains, far from the countries Vokalia and Consonantia, there live the blind texts.</p>
      <div class="card-link">LEARN MORE <svg width="10" height="4" viewBox="0 0 10 4"><path d="M0 2h8M6 .3 9 2 6 3.7" fill="none" stroke="#8a8a8a"/></svg><b></b></div>
    </article>
  </section>

  <div class="abs band-dark" role="img" aria-label="Blurred grey office interior"></div>

  <aside class="abs about-side">
    <div class="abs rule-top"></div>
    <div class="abs side-brand">
      <span class="brand-mark"></span>
      <div><div class="brand-name">VAULTKEY FINDERS</div><div class="brand-url">www.vaultkey-finders.com</div></div>
    </div>
    <div class="abs blog-link">GO CHECK OUR BLOG</div>
    <div class="abs rule-bottom"></div>
  </aside>

  <section class="abs about-main" role="img" aria-label="Dark office scene with people on phones">
    <div class="abs about-eyebrow">ABOUT US</div>
    <div class="abs about-eyebrow-rule"></div>
    <h2 class="abs about-title">VAULT KEY FINDERS</h2>
    <p class="abs about-copy">Far far away, behind the word mountains, far from the countries Vokalia and Consonantia, there live the blind texts. Separated they live in Bookmarksgrove right at the coast of the Semantics, a large language ocean.</p>
    <div class="abs about-dots"><i></i><i></i></div>
    <div class="abs about-media" role="img" aria-label="Hand holding a phone showing a yellow wallet login screen"></div>
  </section>

  <section>
    <h2 class="abs callback-title">Request a callback</h2>
    <p class="abs callback-sub">Get in touch with us, we got your back.</p>
    <div class="abs field" style="left:94px"><label>NAME:</label></div>
    <div class="abs field" style="left:275px"><label>EMAIL</label></div>
    <div class="abs field" style="left:456px"><label>BE ABLE TO :</label></div>
    <div class="abs send">SEND</div>
  </section>

  <footer class="abs footer">
    <p class="abs copyright">COPYRIGHT © 2018 HARBOR LANE STUDIO.<br>ALL RIGHTS RESERVED.</p>
    <div class="abs social"><i></i><i></i></div>
    <p class="abs footer-url">WWW.VAULTKEY-FINDERS.COM</p>
  </footer>

</main>
</body>
</html>
```